Web Design Project - Torvalen Homes

We would like you to refine our web layouts for a (1) homepage and (2) a product page (see attached files for reference).

The client is a swiss construction company, that designs, builds and sells standardized and tailored-made residential houses.

His logo is old, but not up for redesign. The only way to salvage it, is to incorporate its yellow color (as highlight) to the overall design, so as to create some brand awareness.

REQUIREMENTS FOR THE HOMEPAGE:
1. telephone number over menu
2. logo + menu with 6 categories
3. slider for showing various house types (for pics, see attachments)
4. "AKTUELL" card with yellow color (to show his most actual projects) and a strong Call For Action (what in German would be: KONTAKT AUFNEHMEN)
5. a yellow stripe for his company's slogan (Ihr Partner für individuelle und normierte Wohnbauten)
6. A left coloumn with
(a) two picture-holders under the title REFERENZEN
(b) the three supporting logos of ZIRB, KALVORTA and VB DÄMMWERK ALPEN (can be downloaded as pngs)
7. A right column with 6 headlines + texts of 3 lines each
8. a footer with the adress info

REQUIREMENTS FOR PRODUKT PAGE:
1. slider for pictures
2. info box with Call For Action for particular House-types
3. thumbnail pics under the slider for additional images of any particular house type
4. Left-side: name of house type and picture
5. Right-side: Header and blindtext for house description
6. three placeholders for 3 floor plans

NB No coding necessary. An imaginative, fresh design along the layout requirements will do.
Thanx to all

To all those who had probs with the downloading of the attached files:
we've posted a new Zip.
Have a look!
thankx

Thanks to everyone who participated.
We will be showing a selection of your designs to the client within the next couple of days.
We'll get back to you, as soon as possible.

Industry/Entity Type

Construction

Requirements
Must have
• - slider
- info box with call for action
- thumbnail pictures
- fresh look based on colors, design of elements (slider, info box), font selection

```html
<!DOCTYPE html>
<html lang="de">
<head>
<meta charset="utf-8">
<title>Torvalen Homes – Wohnbauten</title>
<link rel="stylesheet" href="https://fonts.googleapis.com/css2?family=Oswald:wght@400;500&family=Ubuntu:wght@400;500&family=Montserrat:wght@300;400&family=Raleway:wght@300&family=Passion+One&display=swap">
<style>
:root{
  --yellow:#fcc400;
  --yellow-soft:#f9d86a;
  --orange:#f5b21a;
  --paper:#efece4;
  --ink:#1c1c1c;
  --text:#5a5650;
  --white:#ffffff;
  --black:#000000;
  --rule:#c9c5bb;
  --footer-link:#8b8b8b;
}
*{box-sizing:border-box;margin:0;padding:0}
html,body{width:700px;height:1200px;overflow:hidden}
body{position:relative;background:var(--paper);font-family:"Ubuntu",sans-serif;color:var(--text)}
.abs{position:absolute}

/* header */
.site-header{left:0;top:0;width:700px;height:63px;background:var(--white);border-bottom:1px solid #dcd8ce}
.brand{left:85px;top:16px;display:flex;align-items:center;gap:5px;font-family:"Oswald",sans-serif;font-weight:500;font-size:15px;color:var(--ink);letter-spacing:.2px}
.brand-mark{width:10px;height:10px;background:var(--yellow)}
.phone{right:87px;top:7px;font-family:"Montserrat",sans-serif;font-weight:300;font-size:20px;color:var(--orange)}
.main-nav{left:250px;top:39px;display:flex;font-family:"Oswald",sans-serif;font-size:14px;color:var(--ink);text-transform:uppercase}
.main-nav a{color:inherit;text-decoration:none;display:block;height:24px;line-height:24px;padding:0 5px;margin-right:4px}
.main-nav a.active{background:var(--yellow);color:var(--white);transform:skewX(-8deg);padding:0 9px}
.main-nav a.active span{display:inline-block;transform:skewX(8deg)}

/* slider */
.slider{left:83px;top:74px;width:535px;height:272px;border:3px solid var(--white);box-shadow:0 0 2px rgba(0,0,0,.25)}
.slider-photo{width:100%;height:100%;background:linear-gradient(180deg,#9fc3e4 0%,#b9c9cf 35%,#a8927a 55%,#6f8a48 75%,#4d6d2c 100%)}
.slider-pager{right:3px;top:96px;width:19px;height:82px;background:var(--white);border-radius:10px 0 0 10px;display:flex;flex-direction:column;align-items:center;justify-content:center;gap:4px}
.slider-pager i{width:9px;height:9px;border:1.5px solid #aaa;border-radius:50%;display:block}
.slider-pager i.on{border-color:var(--yellow);background:var(--white)}

/* frames */
.photo-frame{border:3px solid var(--white);box-shadow:0 0 2px rgba(0,0,0,.2)}
.photo-fill{width:100%;height:100%}
.caption{font-size:9px;color:var(--ink)}

/* left column */
.ref-1{left:82px;top:359px;width:125px;height:70px}
.ref-2{left:82px;top:452px;width:125px;height:71px}
.photo-ref1{background:linear-gradient(180deg,#c8dbe9 0%,#8f8a78 45%,#6f7d4a 100%)}
.photo-ref2{background:linear-gradient(180deg,#8fc0ea 0%,#c7b59a 50%,#5f8d3b 100%)}
.section-tag{left:82px;top:553px;width:126px;height:22px;background:var(--yellow);font-family:"Oswald",sans-serif;font-size:13px;color:var(--ink);line-height:22px;padding-left:5px;text-transform:uppercase}
.partner{left:84px;display:flex;flex-direction:column;align-items:flex-start;gap:3px}
.partner-badge{display:block}
.partner-name{font-size:8px;color:var(--ink);font-weight:500;letter-spacing:.3px}

/* middle column */
.slogan{left:219px;top:358px;width:262px;height:47px;background:var(--yellow);font-family:"Oswald",sans-serif;font-weight:500;font-size:16px;line-height:17px;color:var(--ink);text-align:center;padding-top:6px}
.feature-photo{left:219px;top:417px;width:262px;height:131px}
.photo-feature{background:linear-gradient(180deg,#4d8fd8 0%,#8ab2d9 35%,#8b7f7a 55%,#4f8a2f 78%,#3d7422 100%)}
.welcome-title{left:219px;top:556px;font-family:"Ubuntu",sans-serif;font-weight:500;font-size:19px;color:var(--ink)}
.welcome-text{left:219px;top:582px;width:264px;font-size:8.4px;line-height:12.2px;color:var(--text)}

/* news */
.news{left:492px;top:358px;width:126px;height:368px;background:var(--yellow);padding:6px 8px}
.news-title{font-family:"Oswald",sans-serif;font-size:13px;color:var(--ink);margin-bottom:6px}
.news-item{border-bottom:1px solid rgba(255,255,255,.45);padding:5px 0 6px;height:53px}
.news-item:last-child{border-bottom:none}
.news-date{font-size:7px;color:#a8780a;margin-bottom:2px}
.news-text{font-size:7.2px;line-height:10.2px;color:var(--ink)}

/* projects */
.projects{left:0;top:737px;width:700px;height:156px;background:var(--yellow-soft)}
.projects-title{left:0;top:8px;width:700px;display:flex;align-items:center;justify-content:center;gap:8px;font-family:"Oswald",sans-serif;font-size:19px;color:var(--ink);text-transform:uppercase}
.projects-title .rule{width:175px;height:0;border-top:1px solid #b89a35;border-bottom:1px solid #fbe7a2}
.project{top:47px;width:125px}
.project .photo-frame{height:79px}
.project .caption{margin-top:6px}
.proj-a{background:linear-gradient(180deg,#9ab7d6 0%,#7e7a7e 50%,#3d5680 100%)}
.proj-b{background:linear-gradient(180deg,#4f8ad0 0%,#b9c2c8 50%,#6d8a45 100%)}
.proj-c{background:linear-gradient(180deg,#3f73c8 0%,#56505a 45%,#7ca049 100%)}
.proj-d{background:linear-gradient(180deg,#7fb0e6 0%,#d8d3c8 55%,#6f9a3f 100%)}

/* call to action */
.cta-lead{left:0;top:906px;width:700px;text-align:center;font-family:"Raleway",sans-serif;font-weight:300;font-size:21px;color:#333}
.cta-button{left:233px;top:940px;width:236px;height:43px;background:linear-gradient(180deg,#fdd540 0%,#f7c000 55%,#e7a900 100%);border-radius:4px;box-shadow:0 2px 0 #b88400;font-family:"Passion One",sans-serif;font-size:21px;color:var(--ink);text-align:center;line-height:43px;letter-spacing:.5px}

/* newsletter */
.divider{left:82px;width:536px;height:0;border-top:2px solid var(--rule)}
.newsletter-lead{left:0;top:1017px;width:700px;text-align:center;font-family:"Montserrat",sans-serif;font-size:12.5px;color:#333}
.field{top:1045px;height:29px;background:var(--white);border:1px solid #d8d4cc;font-family:"Montserrat",sans-serif;font-size:8.5px;color:#9a9a9a;line-height:27px;padding-left:9px}
.signup{left:514px;top:1045px;width:81px;height:29px;border:2px solid var(--ink);border-radius:3px;background:var(--white);font-family:"Montserrat",sans-serif;font-size:11px;color:var(--ink);text-align:center;line-height:25px}

/* footer */
.site-footer{left:0;top:1109px;width:700px;height:91px;background:var(--black);border-top:2px solid var(--yellow)}
.social{left:0;top:16px;width:700px;display:flex;justify-content:center;gap:4px}
.social i{width:17px;height:17px;border-radius:50%;background:#8a8a8a;display:block}
.footer-nav{left:0;top:44px;width:700px;display:flex;justify-content:center;gap:12px;font-family:"Oswald",sans-serif;font-size:10px;color:var(--footer-link);text-transform:uppercase}
.copyright{left:0;top:70px;width:700px;text-align:center;font-size:7px;color:#6d6d6d}
</style>
</head>
<body>

<header class="abs site-header">
  <div class="abs brand"><span class="brand-mark"></span>Torvalen Homes</div>
  <div class="abs phone">+381 64 5550192</div>
  <nav class="abs main-nav">
    <a class="active" href="#"><span>Home</span></a>
    <a href="#">About us</a>
    <a href="#">Categories</a>
    <a href="#">Services</a>
    <a href="#">News</a>
    <a href="#">Contact us</a>
  </nav>
</header>

<section class="abs slider">
  <div class="slider-photo" role="img" aria-label="Large stone family house with autumn trees and a green lawn"></div>
  <div class="abs slider-pager"><i class="on"></i><i></i><i></i><i></i><i></i></div>
</section>

<!-- left column -->
<div class="abs ref-1">
  <div class="photo-frame" style="height:70px"><div class="photo-fill photo-ref1" role="img" aria-label="Two-storey house with siding and front lawn"></div></div>
  <div class="caption" style="margin-top:5px">Referenzen</div>
</div>
<div class="abs ref-2">
  <div class="photo-frame" style="height:71px"><div class="photo-fill photo-ref2" role="img" aria-label="Craftsman style house under blue sky"></div></div>
  <div class="caption" style="margin-top:5px">Referenzen</div>
</div>

<div class="abs section-tag">Supporting</div>
<div class="abs partner" style="top:586px">
  <svg class="partner-badge" width="116" height="40" viewBox="0 0 116 40" role="img" aria-label="ZIRB partner badge">
    <rect x="2" y="2" width="112" height="36" rx="6" fill="#6fae4a"/>
  </svg>
  <span class="partner-name">ZIRB</span>
</div>
<div class="abs partner" style="top:650px">
  <svg class="partner-badge" width="122" height="26" viewBox="0 0 122 26" role="img" aria-label="KALVORTA partner badge">
    <rect x="1" y="1" width="120" height="24" fill="#d9262a"/>
  </svg>
  <span class="partner-name">KALVORTA</span>
</div>
<div class="abs partner" style="top:702px">
  <svg class="partner-badge" width="120" height="10" viewBox="0 0 120 10" role="img" aria-label="VB DÄMMWERK ALPEN partner badge">
    <rect x="0" y="0" width="120" height="10" fill="#8e8e8e"/>
  </svg>
  <span class="partner-name">VB DÄMMWERK ALPEN</span>
</div>

<!-- middle column -->
<div class="abs slogan">Ihr Partner für individuelle und<br>normierte Wohnbauten</div>
<div class="abs feature-photo photo-frame" style="border:none;box-shadow:none">
  <div class="photo-fill photo-feature" role="img" aria-label="Large Victorian house with green lawn under a blue sky"></div>
</div>
<h1 class="abs welcome-title">Welcome to Torvalen</h1>
<p class="abs welcome-text">Lorem Ipsum. Proin gravida nibh vel velit auctor aliquet. Aenean sollicitudin, lorem quis bibendum auctor, nisi elit consequat ipsum, nec sagittis sem nibh id elit. Duis sed odio sit amet nibh vulputate cursus a sit amet mauris. Morbi accumsan ipsum velit. Nam nec tellus a odio tincidunt auctor a ornare odio. Sed non &nbsp;mauris vitae erat consequat auctor eu in elit. Class aptent taciti sociosqu ad litora torquent per conubia nostra, per inceptos himenaeos. Mauris in erat justo. Nullam ac urna eu felis dapibus condimentum sit amet a augue. Sed non neque elit. Sed ut imperdiet nisi. Proin condimentum fermentum nunc. Etiam pharetra, erat sed fermentum feugiat, velit mauris egestas quam, ut aliquam massa nisl quis neque. Suspendisse in orci enim.</p>

<!-- news column -->
<aside class="abs news">
  <h2 class="news-title">NEWS</h2>
  <div class="news-item"><div class="news-date">10-03-2013</div><div class="news-text">Lorem ipsum dolor sit amet, consectetur adipisicing elit, sed do eiusmod tempor incididunt...</div></div>
  <div class="news-item"><div class="news-date">10-03-2013</div><div class="news-text">Lorem ipsum dolor sit amet, consectetur adipisicing elit, sed do eiusmod tempor incididunt...</div></div>
  <div class="news-item"><div class="news-date">10-03-2013</div><div class="news-text">Lorem ipsum dolor sit amet, consectetur adipisicing elit, sed do eiusmod tempor incididunt...</div></div>
  <div class="news-item"><div class="news-date">10-03-2013</div><div class="news-text">Lorem ipsum dolor sit amet, consectetur adipisicing elit, sed do eiusmod tempor incididunt...</div></div>
  <div class="news-item"><div class="news-date">10-03-2013</div><div class="news-text">Lorem ipsum dolor sit amet, consectetur adipisicing elit, sed do eiusmod tempor incididunt...</div></div>
  <div class="news-item"><div class="news-date">10-03-2013</div><div class="news-text">Lorem ipsum dolor sit amet, consectetur adipisicing elit, sed do eiusmod tempor incididunt...</div></div>
</aside>

<!-- recent projects -->
<section class="abs projects">
  <div class="abs projects-title">
    <span class="rule"></span>
    <svg width="12" height="12" viewBox="0 0 24 24"><path d="M12 2l2.9 6.6 7.1.6-5.4 4.7 1.6 7L12 17.2 5.8 20.9l1.6-7L2 9.2l7.1-.6z" fill="none" stroke="#a88a2a" stroke-width="1.8"/></svg>
    <span>Recent Project</span>
    <svg width="12" height="12" viewBox="0 0 24 24"><path d="M12 2l2.9 6.6 7.1.6-5.4 4.7 1.6 7L12 17.2 5.8 20.9l1.6-7L2 9.2l7.1-.6z" fill="none" stroke="#a88a2a" stroke-width="1.8"/></svg>
    <span class="rule"></span>
  </div>
  <div class="abs project" style="left:82px"><div class="photo-frame"><div class="photo-fill proj-a" role="img" aria-label="Lakeside house with mountains behind"></div></div><div class="caption">Lorem Ipsum</div></div>
  <div class="abs project" style="left:219px"><div class="photo-frame"><div class="photo-fill proj-b" role="img" aria-label="White villa with driveway"></div></div><div class="caption">Lorem Ipsum</div></div>
  <div class="abs project" style="left:356px"><div class="photo-frame"><div class="photo-fill proj-c" role="img" aria-label="Dark roofed family house with porch"></div></div><div class="caption">Lorem Ipsum</div></div>
  <div class="abs project" style="left:493px"><div class="photo-frame"><div class="photo-fill proj-d" role="img" aria-label="Light family house with garage"></div></div><div class="caption">Lorem Ipsum</div></div>
</section>

<!-- call to action -->
<p class="abs cta-lead">What in german would be</p>
<a class="abs cta-button">KONTAKT AUFNEHMEN</a>

<!-- newsletter -->
<div class="abs divider" style="top:1000px"></div>
<p class="abs newsletter-lead">We write really awesome newsletters. Sign up to stay up to date.</p>
<div class="abs field" style="left:104px;width:199px">Your name</div>
<div class="abs field" style="left:309px;width:199px">Your email</div>
<div class="abs signup">SIGN UP</div>
<div class="abs divider" style="top:1088px"></div>

<!-- footer -->
<footer class="abs site-footer">
  <div class="abs social"><i></i><i></i><i></i></div>
  <nav class="abs footer-nav"><span>Home</span><span>About us</span><span>Categories</span><span>Services</span><span>News</span><span>Contact us</span></nav>
  <p class="abs copyright">Copyright ©2013 Torvalen.</p>
</footer>

</body>
</html>
```